Ledgerforge Studio - WordPress Theme & Logo

Design a logo and Wordpress website design for Ledgerforge Studio. Ledgerforge Studio provides cryptocurrency development services to clients who need a team to create & continue developing a new cryptocurrency or who want to replace their current cryptocurrency development team. more details in the attached document.
Updates

Target Market(s)

Entrepreneurs who are building a business / platform that makes use of an underlying cryptocurrency.

Logo Text

LS or Ledgerforge Studio

Coding

Coded - Design and coding required

Font styles to use
Sans Serif

Requirements
Must have
• Professional logo, complete coded Wordpress theme for all pages, containing all specified links and buttons
Nice to have
• It would be nice if the buttons that are meant to integrate with Dealcurrent contain the necessary code for that. I can provide any necessary Dealcurrent details from my account.
Should not have
• Slow loading time

```html
<!DOCTYPE html>
<html lang="en">
<head>
<meta charset="utf-8">
<title>Ledgerforge Studio</title>
<link rel="stylesheet" href="https://fonts.googleapis.com/css2?family=Montserrat:wght@500;600;700;800&family=Roboto:wght@400;500;700&display=swap">
<style>
:root{
  --navy:#13223a;
  --navy-deep:#0d1a2e;
  --band:#245080;
  --band-dark:#1d3f69;
  --blue:#0d7cf2;
  --blue-soft:#3f86d6;
  --hex:#2f5d93;
  --ink:#111111;
  --text:#333333;
  --muted:#555555;
  --line:#e3e6ea;
  --pale:#f4f5f7;
  --white:#ffffff;
  --star:#f2b600;
}
*{box-sizing:border-box;margin:0;padding:0}
html,body{width:1200px;height:3320px;overflow:hidden}
body{position:relative;background:var(--white);font-family:"Roboto",Arial,sans-serif;color:var(--text)}
.abs{position:absolute}
.heading{font-family:"Montserrat",Arial,sans-serif;font-weight:700;color:var(--ink)}
.btn{position:absolute;display:flex;align-items:center;justify-content:center;background:var(--blue);color:var(--white);border-radius:30px;font-family:"Montserrat",Arial,sans-serif;font-weight:600;font-size:16px}

/* hero */
.hero{position:absolute;left:0;top:0;width:1200px;height:619px;background:linear-gradient(100deg,#1a2d47 0%,#1c3352 45%,#1a3a5c 100%);overflow:hidden}
.hero-visual{position:absolute;left:560px;top:71px;width:640px;height:548px;background:radial-gradient(circle at 55% 45%,#8fd0f0 0%,#3f8fc4 22%,#24557f 50%,rgba(28,51,82,0) 78%)}
.topbar{position:absolute;left:0;top:0;width:1200px;height:71px;background:rgba(16,28,46,.55)}
.brand{position:absolute;display:flex;align-items:center;gap:10px;color:var(--white);font-family:"Montserrat",Arial,sans-serif;font-weight:600}
.brand-mark{background:var(--white)}
.nav-link{position:absolute;top:25px;color:var(--white);font-family:"Roboto",Arial,sans-serif;font-weight:500;font-size:14.5px}
.lang{position:absolute;left:763px;top:25px;width:36px;height:19px;background:#1f3e8a;border:1px solid #d33}
.hero-title{position:absolute;left:98px;top:176px;font-family:"Montserrat",Arial,sans-serif;font-weight:700;font-size:31px;line-height:41.5px;color:var(--white)}
.hero-text{position:absolute;left:98px;top:313px;width:510px;font-size:11.5px;line-height:23px;color:var(--white)}
.slider-next{position:absolute;left:100px;top:569px;color:var(--white);font-size:17px;display:flex;align-items:center;gap:8px}
.slider-count{position:absolute;left:218px;top:545px;color:var(--white);font-family:"Montserrat",Arial,sans-serif;font-weight:700;font-size:62px;display:flex;align-items:center;gap:6px}
.slider-count small{font-size:30px;font-weight:400}

/* section head */
.sec-head{position:absolute;left:0;width:1200px;text-align:center}
.sec-mark{display:block;margin:0 auto;width:22px;height:22px;background:var(--hex)}
.sec-label{display:block;margin-top:8px;font-size:11.5px;color:var(--blue-soft);text-transform:uppercase;letter-spacing:.3px}
.sec-title{display:block;margin-top:6px;font-size:39px}

/* why */
.why-card{position:absolute;top:822px;width:322px;height:306px;border:1px solid var(--line);text-align:center}
.why-card svg{position:absolute;left:109px;top:40px}
.why-card h3{position:absolute;top:178px;left:0;width:100%;font-size:27px}
.why-card p{position:absolute;top:220px;left:30px;right:30px;font-size:15px;line-height:25px;color:var(--ink)}

/* about */
.about{position:absolute;left:0;top:1225px;width:1200px;height:467px;background:var(--band)}
.about-photo{position:absolute;left:102px;top:65px;width:450px;height:343px;background:linear-gradient(90deg,#d9dcdf 0%,#b9bec4 40%,#3a5580 60%,#e8eaec 100%)}
.about-label{position:absolute;left:634px;top:94px;font-size:11.5px;color:var(--white);font-weight:500}
.about-title{position:absolute;left:634px;top:112px;font-size:36px;color:var(--white)}
.about-text{position:absolute;left:634px;top:169px;width:470px;font-size:14.2px;line-height:27.5px;color:var(--white)}
.btn-ghost{position:absolute;left:634px;top:328px;width:155px;height:45px;border:1.5px solid var(--white);border-radius:30px;color:var(--white);display:flex;align-items:center;justify-content:center;font-family:"Montserrat",Arial,sans-serif;font-weight:600;font-size:15px}

/* testimonials */
.reviews{position:absolute;left:0;top:1692px;width:1200px;height:521px;background:var(--pale)}
.review-card{position:absolute;top:1913px;width:322px;height:220px;background:var(--white);text-align:center;box-shadow:0 2px 6px rgba(0,0,0,.04)}
.review-avatar{position:absolute;top:-44px;left:112px;width:98px;height:84px;clip-path:polygon(25% 0,75% 0,100% 50%,75% 100%,25% 100%,0 50%)}
.review-name{position:absolute;top:54px;left:0;width:100%;font-family:"Montserrat",Arial,sans-serif;font-weight:700;font-size:13px;color:var(--ink);letter-spacing:.4px}
.review-stars{position:absolute;top:72px;left:0;width:100%;color:var(--star);font-size:9px;letter-spacing:1px}
.review-text{position:absolute;top:92px;left:20px;right:20px;font-size:13.2px;line-height:22.5px;color:var(--muted)}
.review-quote{position:absolute;left:138px;bottom:-24px;width:46px;height:46px;border-radius:50%;background:var(--blue-soft);display:flex;align-items:center;justify-content:center;color:var(--white);font-family:Georgia,serif;font-size:34px;font-weight:700;line-height:1;padding-top:12px}

/* services */
.services-text{position:absolute;left:184px;top:2388px;width:832px;text-align:center;font-size:14.3px;line-height:27.8px;color:var(--muted)}
.plan{position:absolute;top:2528px;width:317px;height:299px;background:var(--white);box-shadow:0 3px 12px rgba(0,0,0,.06)}
.plan-head{height:86px;background:linear-gradient(110deg,#3f86d6 0%,#3a74b8 55%,#2a5288 100%);display:flex;align-items:center;justify-content:center;text-align:center;color:var(--white);font-family:"Montserrat",Arial,sans-serif;font-weight:800;font-size:25px;line-height:26px}
.plan ul{list-style:none;position:absolute;left:72px;top:114px}
.plan li{display:flex;align-items:center;gap:9px;font-size:15px;color:var(--ink);height:31px}
.plan li i{width:13px;height:13px;border:1.5px solid var(--blue-soft);border-radius:50%;display:flex;align-items:center;justify-content:center}
.plan li i::after{content:"";width:6px;height:6px;border-radius:50%;background:var(--blue-soft)}
.plan .btn{left:68px;top:221px;width:175px;height:46px}

/* footer */
.footer{position:absolute;left:0;top:2909px;width:1200px;height:411px;background:linear-gradient(120deg,var(--navy-deep) 0%,#14233b 60%,#17294a 100%)}
.foot-title{position:absolute;top:72px;font-family:"Montserrat",Arial,sans-serif;font-weight:700;font-size:16.5px;color:var(--white)}
.foot-list{position:absolute;top:104px;list-style:none}
.foot-list li{font-size:15px;color:var(--white);height:33.5px}
.social{position:absolute;top:255px;width:17px;height:17px;border:2px solid var(--white);border-radius:3px}
.news-input{position:absolute;left:808px;top:105px;width:288px;height:49px;border-radius:30px;background:var(--white);padding-left:24px;display:flex;align-items:center;font-size:14px;color:#444}
.news-btn{left:808px;top:163px;width:288px;height:48px;font-weight:700;font-size:15px}
.foot-rule{position:absolute;left:100px;top:290px;width:1000px;height:1px;background:rgba(255,255,255,.45)}
.copyright{position:absolute;left:0;top:316px;width:1200px;text-align:center;font-size:14.3px;color:var(--white)}
</style>
</head>
<body>

<header class="hero">
  <div class="hero-visual" role="img" aria-label="Photo of a businessman facing a glowing globe covered in a network of connected user nodes"></div>
  <div class="topbar"></div>
  <div class="brand" style="left:100px;top:11px;font-size:21px;line-height:22px">
    <span class="brand-mark" style="width:46px;height:46px"></span>
    <span>Ledgerforge<br>Studio</span>
  </div>
  <span class="nav-link" style="left:339px">ABOUT US</span>
  <span class="nav-link" style="left:440px">OUR SERVICES</span>
  <span class="nav-link" style="left:571px">TESTIMONIALS</span>
  <span class="nav-link" style="left:705px">BLOG</span>
  <span class="lang" role="img" aria-label="Language: English"></span>
  <span class="btn" style="left:824px;top:8px;width:274px;height:53px">Schedule a Free Consultation</span>

  <h1 class="hero-title">YOUR OWN CRYPTOCURRENCY.<br>SECURE, EASY TO USE, AND<br>BUILT BY AN EXPERT TEAM.</h1>
  <p class="hero-text">Ledgerforge Studio adds professionalism to cryptocurrency development. Our done-for-you service covers everything from development and IT operations to ongoing support. You haveaccess to a full team, for less than the typical cost of a single developer</p>
  <span class="btn" style="left:99px;top:402px;width:275px;height:53px">Schedule a Free Consultation</span>

  <div class="slider-next">Next
    <svg width="28" height="14" viewBox="0 0 28 14"><path d="M1 7h25M20 1l6 6-6 6" fill="none" stroke="#fff" stroke-width="1.6"/></svg>
  </div>
  <div class="slider-count">01<small>/</small>
    <svg width="32" height="32" viewBox="0 0 32 32"><circle cx="16" cy="16" r="14" fill="none" stroke="#fff" stroke-width="1.6"/><path d="M13 10l6 6-6 6" fill="none" stroke="#fff" stroke-width="1.6"/></svg>
  </div>
  <svg class="abs" style="left:590px;top:561px" width="20" height="40" viewBox="0 0 20 40"><rect x="2" y="1" width="16" height="24" rx="8" fill="none" stroke="#fff" stroke-width="1.4"/><line x1="10" y1="6" x2="10" y2="11" stroke="#fff" stroke-width="1.4"/><path d="M5 31l5 5 5-5" fill="none" stroke="#fff" stroke-width="1.4"/></svg>
</header>

<section aria-label="Why choose us">
  <div class="sec-head" style="top:697px">
    <span class="sec-mark"></span>
    <span class="sec-label">Why choose us</span>
    <h2 class="sec-title heading">Why choose Ledgerforge Studio</h2>
  </div>

  <article class="why-card" style="left:100px">
    <svg width="102" height="117" viewBox="0 0 102 117"><polygon points="51,0 102,29 102,88 51,117 0,88 0,29" fill="#2f5d93"/><path d="M34 50h34l-17 24z M34 50l6-8h22l6 8M44 50l7 24 7-24M40 42l4 8 7-8 7 8 4-8" fill="none" stroke="#fff" stroke-width="2" stroke-linejoin="round"/><path d="M51 30v6M40 33l3 4M62 33l-3 4" stroke="#fff" stroke-width="2"/></svg>
    <h3 class="heading">Value</h3>
    <p>A team of experts, regular updates, and fixed costs</p>
  </article>
  <article class="why-card" style="left:440px">
    <svg width="102" height="117" viewBox="0 0 102 117"><polygon points="51,0 102,29 102,88 51,117 0,88 0,29" fill="#2f5d93"/><circle cx="45" cy="58" r="9" fill="none" stroke="#fff" stroke-width="2"/><path d="M30 80c2-9 9-13 15-13s13 4 15 13" fill="none" stroke="#fff" stroke-width="2"/><path d="M56 36h18v12h-10l-5 5v-5h-3z" fill="none" stroke="#fff" stroke-width="2" stroke-linejoin="round"/></svg>
    <h3 class="heading">Support</h3>
    <p>Receive advice and other services, beyond development.</p>
  </article>
  <article class="why-card" style="left:779px">
    <svg width="102" height="117" viewBox="0 0 102 117"><polygon points="51,0 102,29 102,88 51,117 0,88 0,29" fill="#2f5d93"/><circle cx="51" cy="44" r="8" fill="none" stroke="#fff" stroke-width="2"/><circle cx="51" cy="44" r="3" fill="#fff"/><circle cx="38" cy="62" r="5" fill="none" stroke="#fff" stroke-width="2"/><circle cx="64" cy="62" r="5" fill="none" stroke="#fff" stroke-width="2"/><path d="M28 80c1-7 5-11 10-11s9 4 10 11M54 80c1-7 5-11 10-11s9 4 10 11" fill="none" stroke="#fff" stroke-width="2"/></svg>
    <h3 class="heading">Commitment</h3>
    <p>Enjoy regular updates and new features</p>
  </article>
</section>

<section class="about" aria-label="About us">
  <div class="about-photo" role="img" aria-label="Photo of a smiling businessman in a blue blazer holding a tablet in an office"></div>
  <span class="about-label">ABOUT US</span>
  <h2 class="about-title heading">Who We Are</h2>
  <p class="about-text">in addition to creating and enhancing cryptocurrencies for clients, the Ledgerforge Studio team has been running the Corvane cryptocurrency since 2017. We prefer long-term relationships, enabling us to deliver the very highest quality and giving you peace of mind that you've got a professional and trustworthy team at your side.</p>
  <span class="btn-ghost">Learn More</span>
</section>

<section class="reviews" aria-label="Testimonials">
  <div class="sec-head" style="top:66px">
    <span class="sec-mark"></span>
    <span class="sec-label">Client review</span>
    <h2 class="sec-title heading">Testimonials</h2>
  </div>
</section>
<article class="review-card" style="left:100px">
  <div class="review-avatar" role="img" aria-label="Client portrait" style="background:linear-gradient(160deg,#7fa9cf,#3d6f9f)"></div>
  <div class="review-name">JOHN SMITH</div><div class="review-stars">★★★★★</div>
  <p class="review-text">At vero eos et accusamus etto odio dignissimos ducimus qui blanditiis praesentium voluptatum deleniti atque corrupti qures et quas molestias excepturi sint occaecati</p>
  <div class="review-quote">“</div>
</article>
<article class="review-card" style="left:439px">
  <div class="review-avatar" role="img" aria-label="Client portrait" style="background:linear-gradient(160deg,#f2f2f2,#c9b8a8)"></div>
  <div class="review-name">JOHN SMITH</div><div class="review-stars">★★★★★</div>
  <p class="review-text">At vero eos et accusamus etto odio dignissimos ducimus qui blanditiis praesentium voluptatum deleniti atque corrupti qures et quas molestias excepturi sint occaecati</p>
  <div class="review-quote">“</div>
</article>
<article class="review-card" style="left:778px">
  <div class="review-avatar" role="img" aria-label="Client portrait" style="background:linear-gradient(160deg,#e6e6e6,#4a5a78)"></div>
  <div class="review-name">JOHN SMITH</div><div class="review-stars">★★★★★</div>
  <p class="review-text">At vero eos et accusamus etto odio dignissimos ducimus qui blanditiis praesentium voluptatum deleniti atque corrupti qures et quas molestias excepturi sint occaecati</p>
  <div class="review-quote">“</div>
</article>

<section aria-label="Our service">
  <div class="sec-head" style="top:2275px">
    <span class="sec-mark"></span>
    <span class="sec-label">Our service</span>
    <h2 class="sec-title heading">What We Do</h2>
  </div>
  <p class="services-text">Ledgerforge Studio offers more than just development. We provide a complete solution and our clients receive access to expert advice, ongoing support, I.T. operations, mobile wallets, and even the creation of white papers, Our packages can be tailored to suit you to match your requirements or budget, you can simply pick and choose the features you would like. Alternatively, We can create a custom package just for you.</p>

  <article class="plan" style="left:100px">
    <div class="plan-head">Ledgerforge<br>Creation &amp; Launch</div>
    <ul><li><i></i>This is a list item</li><li><i></i>Another list item</li><li><i></i>Yup, another list item</li></ul>
    <span class="btn">Learn More</span>
  </article>
  <article class="plan" style="left:442px">
    <div class="plan-head">Basic</div>
    <ul><li><i></i>This is a list item</li><li><i></i>Another list item</li><li><i></i>Yup, another list item</li></ul>
    <span class="btn">Learn More</span>
  </article>
  <article class="plan" style="left:783px">
    <div class="plan-head">Mid-range</div>
    <ul><li><i></i>This is a list item</li><li><i></i>Another list item</li><li><i></i>Yup, another list item</li></ul>
    <span class="btn">Learn More</span>
  </article>
</section>

<footer class="footer">
  <span class="abs" style="left:156px;top:58px;width:100px;height:100px;background:var(--white)"></span>
  <span class="abs" style="left:100px;top:208px;width:215px;text-align:center;font-family:'Montserrat',Arial,sans-serif;font-weight:600;font-size:21px;color:var(--white)">Ledgerforge Studio</span>
  <span class="social" style="left:139px" role="img" aria-label="Social link"></span>
  <span class="social" style="left:183px" role="img" aria-label="Social link"></span>
  <span class="social" style="left:224px" role="img" aria-label="Social link"></span>
  <span class="social" style="left:264px" role="img" aria-label="Social link"></span>

  <h4 class="foot-title" style="left:357px">Site Content</h4>
  <ul class="foot-list" style="left:357px"><li>Home</li><li>About</li><li>Feature</li><li>Pricing</li><li>Contact</li></ul>

  <h4 class="foot-title" style="left:581px">Major Topics</h4>
  <ul class="foot-list" style="left:581px"><li>Search</li><li>T&amp;Cs</li><li>Privacy</li><li>Commu</li></ul>

  <h4 class="foot-title" style="left:808px">Get our Newsletter</h4>
  <div class="news-input">Enter your email</div>
  <span class="btn news-btn">SUBSCRIBE</span>

  <div class="foot-rule"></div>
  <p class="copyright">Copyright © 2021 Ledgerforge Studio. All rights reserved.</p>
</footer>

</body>
</html>
```